Alternative Health Practice - Website redesign

With regard to the welcome image, stock photos can't show the faces of other people. And please don't submit a design for a one-page website.
Hello, I am redesigning a website and need some help from a professional.
The old website is here: peter-lindqvist.net (pls note I don't want to reuse the welcome photo from the old site). Much of the written content will remain the same, so note that I also need a page layout/text colour etc that works for text heavy pages: ie www.peter-lindqvist.net/somatic-articles and www.peter-lindqvist.net/client-reviews
My effort at redesigning is underway here: https://pjlindqvist.sitebuildr.net/my-site-7
The original sitebuildr template is this one: https://www.sitebuildr.net/website-template/view/html/2868?originUrl=https%3A%2F%2Fwww.sitebuildr.net%2Fwebsite%2Ftemplates%2Fhtml%2Fhealth-wellness&tpClick=view_button&esi=6305f015-f1b5-4bdd-8dfa-47b7d756bb68
I'm pretty happy with the colour palette. My name Peter Johan Lindqvist is now the "brand" without Rooted Stillness subtitle. Regarding the Welcome section, if you are going to use my photos, it probably needs to be those two that are already there. If you want to put a stock photo there instead, that's fine.
If you want to propose something quite different to my design, I'm happy to receive design files in Photoshop or whatever and then subsequently replicate on Sitebuildr. Up to you.
Target Market(s)
Mostly women, some men ages 28-60.
Coding
Coded - Design and coding required
Number of Pages Required
5+ page
Look and feel
Each slider illustrates characteristics of the customer's brand and the style your logo design should communicate.

```html
<!DOCTYPE html>
<html lang="en">
<head>
<meta charset="utf-8">
<title>Peter Johan Lindqvist</title>
<link href="https://fonts.googleapis.com/css2?family=Urbanist:wght@300;400;500;600;700&family=Parisienne&display=swap" rel="stylesheet">
<style>
:root{
  --bg:#363d31;
  --bg-deep:#2e3429;
  --bg-darker:#2a2f26;
  --sage:#8b9673;
  --frame:#8d9c80;
  --text:#e8e8de;
  --text-soft:#c9cbbd;
  --gold-a:#d1a94e;
  --gold-b:#9b7130;
  --line:#9aa08a;
}
*{margin:0;padding:0;box-sizing:border-box}
html,body{width:1200px;height:3602px;overflow:hidden}
body{position:relative;background:var(--bg);font-family:'Urbanist',sans-serif;color:var(--text)}
.abs{position:absolute}
section,header,footer{position:absolute;left:0;width:1200px}
.btn{position:absolute;height:46px;border-radius:23px;display:flex;align-items:center;justify-content:center;font-size:19px;font-weight:600;color:#fff;background:linear-gradient(90deg,var(--gold-a),var(--gold-b));text-decoration:none}
.btn-outline{background:none;border:1.5px solid var(--line);color:var(--text-soft);font-weight:500}
.heading{font-weight:600;color:var(--sage);font-size:46px;line-height:1.15}
.script{font-family:'Parisienne',cursive;color:var(--sage)}
.body-text{font-size:19px;font-weight:300;line-height:26.6px;color:var(--text)}
.photo{position:absolute;border-radius:10px}
.frame{position:absolute;background:var(--frame);border-radius:10px}

/* header */
.site-header{top:0;height:140px}
.brand{position:absolute;left:84px;top:47px;display:flex;align-items:center;gap:12px;font-size:25px;font-weight:600;color:var(--text)}
.brand-dot{width:44px;height:44px;border-radius:50%;background:#b48a3c}
.nav{position:absolute;right:84px;top:56px;display:flex;gap:35px;font-size:20px;font-weight:400;color:var(--text-soft)}

/* hero */
.hero{top:0;height:821px;background:var(--bg)}
.cloud{position:absolute;width:91px;height:50px;border:1.5px solid var(--line);border-radius:25px 25px 22px 22px/28px 28px 22px 22px;display:flex;align-items:center;justify-content:center;font-family:'Parisienne',cursive;font-size:17px;color:var(--text-soft)}

/* about */
.about{top:821px;height:711px;background:linear-gradient(180deg,#313729,#2b3026 60%,#30362b)}
/* practice */
.practice{top:1532px;height:534px;background:var(--bg)}
/* reviews */
.reviews{top:2066px;height:558px;background:linear-gradient(180deg,#2f3529,#343a2f 50%,#2c3127)}
.review-card{position:absolute;left:152px;top:188px;width:896px;height:205px;border:1.5px solid var(--line);border-radius:14px}
.arrow{position:absolute;width:32px;height:32px}
/* contact */
.contact{top:2624px;height:547px;background:var(--bg)}
.field{position:absolute;width:249px;border-bottom:1.5px solid var(--line);padding-bottom:8px;font-size:19px;font-weight:300;color:var(--text-soft)}
.field-wide{width:541px}
/* footer */
.site-footer{top:3171px;height:431px;background:linear-gradient(180deg,#2f3429,#2a2f25)}
.foot-title{position:absolute;top:67px;font-size:24px;font-weight:600;color:var(--text)}
.foot-list{position:absolute;top:106px;list-style:none;font-size:19px;font-weight:300;color:var(--text-soft);line-height:39px}
.social{width:26px;height:26px;border-radius:50%;border:2px solid var(--text)}
</style>
</head>
<body>

<section class="hero">
  <h1 class="heading abs" style="left:84px;top:218px;width:520px">A Body-Centred Path to Healing and Growth</h1>
  <p class="body-text abs" style="left:84px;top:343px;width:440px">I offer an approach to growth and healing which allows for lost and hidden parts of ourselves to come forward and become whole.</p>
  <a class="btn" style="left:84px;top:449px;width:182px">Book a Session</a>
  <div class="frame" style="left:656px;top:172px;width:461px;height:401px"></div>
  <div class="photo" role="img" aria-label="Therapist gently cradling a resting client's head during a session" style="left:639px;top:155px;width:463px;height:403px;background:linear-gradient(135deg,#7d8a79,#e8e6e2 50%,#c9a48e)"></div>

  <div class="cloud" style="left:84px;top:686px">Balance</div>
  <div class="cloud" style="left:202px;top:660px">Purpose</div>
  <div class="cloud" style="left:320px;top:686px">Clarity</div>
  <div class="cloud" style="left:437px;top:660px">Harmony</div>
  <div class="cloud" style="left:555px;top:686px">Discovery</div>
  <div class="cloud" style="left:672px;top:660px">Presence</div>
  <div class="cloud" style="left:790px;top:686px">Success</div>
  <div class="cloud" style="left:908px;top:660px">Creativity</div>
  <div class="cloud" style="left:1025px;top:686px">Ease</div>
</section>

<header class="site-header">
  <div class="brand"><span class="brand-dot"></span>Peter Johan Lindqvist</div>
  <nav class="nav"><span>The Practice</span><span>Feedback</span><span>Approach</span><span>About Me</span><span>Contact</span></nav>
</header>

<section class="about">
  <div class="frame" style="left:127px;top:99px;width:353px;height:528px"></div>
  <div class="photo" role="img" aria-label="Portrait of the practitioner outdoors among greenery" style="left:143px;top:84px;width:351px;height:527px;background:linear-gradient(160deg,#8fa27a,#6b6a4c 50%,#4f553a)"></div>
  <h2 class="heading abs" style="left:537px;top:118px">Peter Johan Lindqvist</h2>
  <p class="script abs" style="left:537px;top:178px;font-size:29px">Rooted Stillness Teacher</p>
  <div class="abs" style="left:537px;top:235px;width:540px">
    <p class="body-text">Growing up in Scotland, I had a strong connection with nature and the outdoors. Playing outside with friends, with bikes, ball sports, and later mountaineering and rock climbing, was what most interested me.</p>
    <p class="body-text" style="margin-top:26px">I studied at Northgate University and worked in London for a number of years as a civil servant. I subsequently set up a property business and in 2006, relocated to Spain.</p>
    <p class="body-text" style="margin-top:26px">At thirty years of age, I found that my life had become quite...</p>
  </div>
  <a class="btn" style="left:537px;top:534px;width:147px">Read more</a>
</section>

<section class="practice">
  <h2 class="heading abs" style="left:84px;top:104px">The Practice</h2>
  <p class="body-text abs" style="left:84px;top:174px;width:525px">Guided by your intention, I will use skills based in touch, movement and perception to facilitate greater congruence between your energy and your physical body. Via this deep listening to the body we will stimulate your natural capacity for healing and growth and you may discover something new about yourself.</p>
  <a class="btn btn-outline" style="left:84px;top:363px;width:152px">Learn more</a>
  <a class="btn" style="left:262px;top:363px;width:181px">Book a Session</a>
  <div class="frame" style="left:687px;top:100px;width:430px;height:350px"></div>
  <div class="photo" role="img" aria-label="Practitioner's hands resting on a client's abdomen during bodywork" style="left:670px;top:83px;width:432px;height:353px;background:linear-gradient(135deg,#8e8672,#d9c2bd 45%,#3b3a58)"></div>
</section>

<section class="reviews">
  <h2 class="heading abs" style="left:0;width:1200px;text-align:center;top:74px">Our Reviews</h2>
  <p class="script abs" style="left:0;width:1200px;text-align:center;top:128px;font-size:29px">Hear from clients that have come to my practice</p>
  <svg class="arrow" style="left:68px;top:276px" viewBox="0 0 32 32" fill="none" stroke="#c9cbbd" stroke-width="1.5"><circle cx="16" cy="16" r="15"/><path d="M22 16H10M15 11l-5 5 5 5"/></svg>
  <svg class="arrow" style="left:1100px;top:276px" viewBox="0 0 32 32" fill="none" stroke="#c9cbbd" stroke-width="1.5"><circle cx="16" cy="16" r="15"/><path d="M10 16h12M17 11l5 5-5 5"/></svg>
  <div class="review-card">
    <div class="abs" role="img" aria-label="Photo of the reviewing client" style="left:27px;top:25px;width:154px;height:154px;border-radius:50%;background:radial-gradient(circle at 50% 45%,#b08a70,#6b7a4c 70%)"></div>
    <svg class="abs" style="left:214px;top:24px" width="36" height="26" viewBox="0 0 36 26" fill="#b48a3c"><circle cx="8" cy="17" r="8"/><path d="M1 16C1 7 6 2 13 1l1 3C9 6 6 9 6 15z"/><circle cx="27" cy="17" r="8"/><path d="M20 16c0-9 5-14 12-15l1 3c-5 2-8 5-8 11z"/></svg>
    <p class="body-text abs" style="left:214px;top:73px;width:660px">You have given me a lot of confidence in myself. You are showing me a new way of life. And I've learned that it is possible to handle the physical pain caused by our emotions. I didn't know how to cope with it.&nbsp; Thank you...</p>
    <p class="abs" style="left:214px;top:163px;font-size:18px;font-weight:600;color:var(--sage)">Lucía Moreno Vidal</p>
  </div>
  <a class="btn" style="left:502px;top:429px;width:196px">Read all reviews</a>
</section>

<section class="contact">
  <div class="abs" role="img" aria-label="Faint leaf decoration" style="left:0;top:138px;width:140px;height:270px;background:radial-gradient(ellipse at 20% 50%,rgba(120,128,108,.45),rgba(54,61,49,0) 70%)"></div>
  <div class="abs" role="img" aria-label="Faint leaf decoration" style="right:0;top:138px;width:140px;height:270px;background:radial-gradient(ellipse at 80% 50%,rgba(120,128,108,.45),rgba(54,61,49,0) 70%)"></div>
  <h2 class="heading abs" style="left:0;width:1200px;text-align:center;top:74px">Contact Peter</h2>
  <p class="body-text abs" style="left:0;width:1200px;text-align:center;top:140px">Contact me for more information about intensives<br>or to arrange an appointment.</p>
  <div class="field" style="left:329px;top:231px">First name</div>
  <div class="field" style="left:621px;top:231px">Last name</div>
  <div class="field" style="left:329px;top:291px">Phone</div>
  <div class="field" style="left:621px;top:291px">Email</div>
  <div class="field field-wide" style="left:329px;top:351px">How can i help?</div>
  <a class="btn" style="left:543px;top:416px;width:114px">Submit</a>
</section>

<footer class="site-footer">
  <div class="abs" style="left:84px;top:56px;display:flex;align-items:center;gap:12px;font-size:25px;font-weight:600;line-height:29px;color:var(--text)"><span class="brand-dot"></span><span>Peter Johan<br>Lindqvist</span></div>
  <h3 class="foot-title" style="left:438px">Quick Links</h3>
  <ul class="foot-list" style="left:438px"><li>Home</li><li>The Practice</li><li>Feedback</li><li>Approach</li><li>Contact</li><li>Blog</li></ul>
  <h3 class="foot-title" style="left:681px">Contact Us</h3>
  <div class="foot-list" style="left:681px;line-height:26.6px">
    <p>Tel: (+351) 900 000 123</p>
    <p style="margin-top:26px">E: info@peter-lindqvist.net</p>
    <p style="margin-top:26px">Rua das Flores 12B<br>Bairro Alto<br>Lisbon 1200-195</p>
  </div>
  <h3 class="foot-title" style="left:1032px">Socials</h3>
  <div class="abs" style="left:1032px;top:110px;display:flex;gap:12px">
    <span class="social" aria-label="Social profile"></span><span class="social" aria-label="Social profile"></span>
  </div>
  <div class="abs" style="left:0;top:380px;width:1200px;border-top:1px solid rgba(154,160,138,.35)"></div>
  <p class="abs" style="left:0;width:1200px;text-align:center;top:396px;font-size:16px;font-weight:300;color:var(--text-soft)">© 2025 Peter Johan Lindqvist</p>
</footer>

</body>
</html>
```